Lindon Business Card

I need a nice and sleek business card.

I need it to promote our website, our rateo page, and or snapgrid page

Snapgrid would be: @lindonjoinery
website would be: www.lindonjoinery-example.com
rateo would be: Lindon Joinery Inc (logo is fine)

Here are a list of service we offer.
1. Custom Kitchen Remodeling
2. Custom Bathroom Remodeling
3. Custom Closet Remodeling
4. Custom Bedroom Remodeling
5. Custom Bars
6. Custom Bookcases
7. Custom Staircases
8. Custom Ceilings

Please use the wording "Every Grain Craft"
We also have been in business since 1992
and we have been serving the rich and famous since.

We do all types of designs, modern and renaissance.

Contact Information for Business Card

Lindon Joinery, Inc.
48715 Brightwell Av,. Unit 305-306
Harlow Vale, CA. 90999
Telmo Dane Ferucci - CEO
818-555-0143
lindonjoinery@mailbox-example.com

```html
<!DOCTYPE html>
<html lang="en">
<head>
<meta charset="utf-8">
<title>Lindon Business Card</title>
<link rel="stylesheet" href="https://fonts.googleapis.com/css2?family=Cormorant+Garamond:ital,wght@1,500&family=Libre+Baskerville:wght@400&display=swap">
<style>
  :root {
    --page: #f4f3f2;
    --card-dark: #2b1b13;
    --card-dark-deep: #1f130d;
    --copper: #c8733b;
    --copper-dark: #7a3a1a;
    --ink-light: #ddd3c9;
    --ink-white: #f7f1ea;
    --wood-light: #c7703a;
    --wood-mid: #9a4a22;
    --wood-dark: #4a2210;
    --veil: rgba(38, 20, 10, 0.5);
    --veil-strong: rgba(30, 15, 8, 0.6);
    --rateo-red: #c8372d;
  }
  * { box-sizing: border-box; margin: 0; padding: 0; }
  html, body { width: 1200px; height: 900px; overflow: hidden; background: var(--page); }
  .canvas { position: relative; width: 1200px; height: 900px; }

  .card {
    position: absolute; top: 295px; width: 540px; height: 310px;
    border-radius: 22px; overflow: hidden;
    box-shadow: 0 14px 30px rgba(0,0,0,0.18);
    font-family: "Libre Baskerville", Georgia, serif;
  }

  /* Front */
  .card-front { left: 40px; background: linear-gradient(160deg, var(--card-dark) 0%, var(--card-dark-deep) 100%); }
  .brand-mark {
    position: absolute; left: 50%; top: 28px; transform: translateX(-50%);
    width: 72px; height: 72px; border: 1.5px solid #9c8c7c; border-radius: 50%;
    display: flex; align-items: center; justify-content: center; text-align: center;
    color: #b8a896; font-size: 9px; line-height: 1.3;
  }
  .company-name {
    position: absolute; top: 120px; width: 100%; text-align: center;
    color: var(--ink-light); font-size: 11px; letter-spacing: 3px;
  }
  .copper-band {
    position: absolute; top: 156px; left: 0; right: 0; height: 9px;
    background: linear-gradient(90deg, var(--copper-dark), var(--copper) 50%, var(--copper-dark));
  }
  .person { position: absolute; top: 196px; left: 24px; width: 160px; text-align: right; color: var(--ink-light); }
  .person-name { font-size: 13.5px; }
  .person-role { font-size: 10px; margin-top: 3px; }
  .divider { position: absolute; left: 196px; top: 186px; width: 1px; height: 90px; background: #8a7a6c; }
  .contact { position: absolute; left: 208px; top: 184px; color: var(--ink-light); font-size: 13.5px; line-height: 1.35; }
  .contact-line { display: flex; align-items: center; gap: 6px; }
  .contact-line svg { width: 15px; height: 15px; flex: none; fill: var(--copper); }
  .address { padding-left: 21px; font-size: 13px; }

  /* Back */
  .card-back { left: 620px; }
  .wood-photo {
    position: absolute; inset: 0;
    background: linear-gradient(110deg, var(--wood-dark) 0%, var(--wood-mid) 30%, var(--wood-light) 60%, var(--wood-mid) 85%, var(--wood-dark) 100%);
  }
  .services-panel { position: absolute; left: 22px; top: 0; width: 238px; height: 232px; background: var(--veil); padding: 22px 0 0 14px; color: var(--ink-white); }
  .tagline { font-family: "Cormorant Garamond", Georgia, serif; font-style: italic; font-weight: 500; font-size: 23px; text-align: center; margin-bottom: 6px; padding-right: 14px; }
  .service-list { list-style: none; font-family: "Cormorant Garamond", Georgia, serif; font-style: italic; font-weight: 500; font-size: 16.5px; line-height: 20.5px; white-space: nowrap; }
  .footer-band { position: absolute; left: 0; right: 0; top: 232px; height: 56px; background: var(--veil-strong); color: var(--ink-white); }
  .social { position: absolute; left: 28px; font-size: 11.5px; display: flex; align-items: center; gap: 6px; white-space: nowrap; }
  .social-snapgrid { top: 8px; }
  .social-rateo { top: 31px; }
  .social-square { width: 15px; height: 15px; border-radius: 3px; background: var(--ink-white); }
  .social-rateo .social-square { background: var(--rateo-red); }
  .website { position: absolute; right: 20px; top: 13px; font-size: 13.5px; letter-spacing: 1.2px; white-space: nowrap; }
</style>
</head>
<body>
<main class="canvas">
  <section class="card card-front">
    <div class="brand-mark">Lindon<br>Joinery</div>
    <div class="company-name">LINDON JOINERY INC.</div>
    <div class="copper-band"></div>
    <div class="person">
      <div class="person-name">Telmo Dane Ferucci</div>
      <div class="person-role">CEO</div>
    </div>
    <div class="divider"></div>
    <div class="contact">
      <div class="contact-line">
        <svg viewBox="0 0 24 24" aria-hidden="true"><path d="M6.6 10.8a15 15 0 0 0 6.6 6.6l2.2-2.2a1 1 0 0 1 1-.25 11.4 11.4 0 0 0 3.6.6 1 1 0 0 1 1 1V20a1 1 0 0 1-1 1A17 17 0 0 1 3 4a1 1 0 0 1 1-1h3.5a1 1 0 0 1 1 1c0 1.25.2 2.45.57 3.570a1 1 0 0 1-.25 1z"/></svg>
        <span>818-555-0143</span>
      </div>
      <div class="contact-line">
        <svg viewBox="0 0 24 24" aria-hidden="true"><path d="M3 6h18v12H3z M3 6l9 7 9-7" fill="none" stroke="#c8733b" stroke-width="2"/></svg>
        <span>lindonjoinery@mailbox-example.com</span>
      </div>
      <div class="contact-line">
        <svg viewBox="0 0 24 24" aria-hidden="true"><path d="M12 3l10 9h-3v8h-5v-5h-4v5H5v-8H2z"/></svg>
        <span>Lindon Joinery, Inc.</span>
      </div>
      <div class="address">48715 Brightwell Av,. Unit 305-306<br>Harlow Vale, CA. 90999</div>
    </div>
  </section>

  <section class="card card-back">
    <div class="wood-photo" role="img" aria-label="Photograph of richly carved wooden interior paneling and columns"></div>
    <div class="services-panel">
      <h1 class="tagline">"Every Grain Craft"</h1>
      <ol class="service-list">
        <li>1. Custom Kitchen Remodeling</li>
        <li>2. Custom Bathroom Remodeling</li>
        <li>3. Custom Closet Remodeling</li>
        <li>4. Custom Bedroom Remodeling</li>
        <li>5. Custom Bars</li>
        <li>6. Custom Bookcases</li>
        <li>7. Custom Staircases</li>
        <li>8. Custom Ceilings</li>
      </ol>
    </div>
    <div class="footer-band">
      <div class="social social-snapgrid"><span class="social-square"></span><span>snapgrid @lindonjoinery</span></div>
      <div class="social social-rateo"><span class="social-square"></span><span>rateo Lindon Joinery Inc</span></div>
      <div class="website">www.lindonjoinery-example.com</div>
    </div>
  </section>
</main>
</body>
</html>
```